Email Signature

We want a new email signature designed that will include an employees picture and our logo at minimum. Of course contact info as well.

For the sample please create the new signature for Dale Prewitt...extra pics provided
please visit our website www.BrightwayUpkeep.com

Need to limit links to our website....government email servers strip out many.
Updates

I have a new draft design I'd like to work from...simple and clean.Needs:LogoDisclaimerand a bit of colorI'd like to make selection this week. Added Tuesday, October 24, 2017

Target Market(s)

other professional businesses

Requirements
Must have
• picture & Logo
• new look and something that auto scales to the emails window.
• Would like to have a new tag line "

```html
<!DOCTYPE html>
<html lang="en">
<head>
<meta charset="utf-8">
<title>Email Signature – Dale Prewitt</title>
<link rel="stylesheet" href="https://fonts.googleapis.com/css2?family=Dancing+Script:wght@500&family=Open+Sans:wght@400&family=Roboto:wght@400;700&display=swap">
<style>
  :root {
    --red: #e01e2b;
    --blue: #24398c;
    --navy: #1b3170;
    --grey-text: #9a9a9a;
    --rule: #e4505a;
    --page: #ffffff;
  }
  * { margin: 0; padding: 0; box-sizing: border-box; }
  html, body { width: 1200px; height: 944px; overflow: hidden; background: var(--page); }
  .signature {
    position: absolute; left: 59px; top: 229px; width: 1082px; height: 486px;
    font-family: "Open Sans", Arial, sans-serif;
  }
  .top-rule { position: absolute; left: 0; top: 0; width: 1082px; height: 2px; background: var(--rule); }
  .portrait {
    position: absolute; left: 4px; top: 9px; width: 230px; height: 311px;
    background: linear-gradient(180deg, #f4f4f4 0%, #d9d4d0 35%, #2a2d3a 70%, #1c1f2a 100%);
  }
  .sig-script {
    position: absolute; left: 270px; top: 108px;
    font-family: "Dancing Script", cursive; font-size: 24px; color: var(--blue);
  }
  .name {
    position: absolute; left: 270px; top: 142px;
    font-family: "Roboto", Arial, sans-serif; font-weight: 700; font-size: 28px; color: var(--red);
  }
  .role {
    position: absolute; left: 270px; top: 178px;
    font-family: "Roboto", Arial, sans-serif; font-size: 20px; color: var(--blue);
  }
  .icon { position: absolute; width: 34px; height: 34px; }
  .phone-icon { left: 270px; top: 220px; }
  .mail-icon { left: 270px; top: 259px; }
  .phone {
    position: absolute; left: 322px; top: 222px; font-size: 22px; color: var(--blue); letter-spacing: 0.5px;
  }
  .company-name {
    position: absolute; left: 660px; top: 52px; width: 400px; text-align: center;
    font-family: "Roboto", Arial, sans-serif; font-weight: 700; font-size: 38px; color: var(--red);
  }
  .pin-icon { left: 694px; top: 170px; }
  .address {
    position: absolute; left: 750px; top: 170px; font-size: 18px; line-height: 25px; color: var(--blue);
  }
  .web-icon { left: 692px; top: 251px; }
  .website { position: absolute; left: 752px; top: 256px; font-size: 19px; color: var(--blue); }
  .band-rule { position: absolute; left: 0; top: 320px; width: 1082px; height: 5px; background: var(--red); }
  .link-band { position: absolute; left: 0; top: 325px; width: 1082px; height: 36px; background: var(--navy); }
  .band-link { position: absolute; top: 9px; display: flex; align-items: center; gap: 14px; color: #fff; font-family: Arial, sans-serif; font-size: 13px; }
  .band-link .dot { width: 22px; height: 22px; border-radius: 50%; background: var(--red); }
  .disclaimer {
    position: absolute; left: 6px; top: 370px; width: 1074px;
    font-family: Arial, Helvetica, sans-serif; font-size: 13.4px; line-height: 19px; color: var(--grey-text);
  }
</style>
</head>
<body>
<section class="signature">
  <div class="top-rule"></div>
  <div class="portrait" role="img" aria-label="Portrait photo of Dale Prewitt in a dark suit, arms crossed"></div>

  <div class="sig-script">Dale M. Prewitt</div>
  <div class="name">Dale Prewitt</div>
  <div class="role">Vice President</div>

  <svg class="icon phone-icon" viewBox="0 0 34 34" aria-hidden="true">
    <circle cx="17" cy="17" r="16" fill="var(--red)"/>
    <path d="M11 8c1-1 2-1 3 0l2 3c.6 1 .3 2-.5 2.6l-1 .8c1 2.4 2.8 4.3 5.2 5.4l.8-1c.6-.8 1.7-1 2.6-.4l3 2c1 .7 1 2 0 3l-1.4 1.4c-1.4 1.4-4 1.2-7-.8-3-2-5.6-4.8-7.4-8-1.6-3-1.8-5.4-.6-6.6z" fill="#fff"/>
  </svg>
  <div class="phone">410-555-0146</div>

  <svg class="icon mail-icon" viewBox="0 0 34 34" aria-hidden="true">
    <circle cx="17" cy="17" r="15" fill="none" stroke="var(--red)" stroke-width="3"/>
    <rect x="9" y="11" width="16" height="12" rx="1" fill="none" stroke="var(--red)" stroke-width="2.2"/>
    <path d="M9.5 11.5 17 18l7.5-6.5M9.5 22.5l5.5-5M24.5 22.5l-5.5-5" fill="none" stroke="var(--red)" stroke-width="2"/>
  </svg>

  <div class="company-name">Brightway Upkeep</div>

  <svg class="icon pin-icon" viewBox="0 0 34 34" aria-hidden="true">
    <circle cx="17" cy="17" r="16" fill="var(--red)"/>
    <path d="M17 6c-4.4 0-8 3.4-8 7.8 0 5.6 8 14.2 8 14.2s8-8.6 8-14.2C25 9.4 21.4 6 17 6z" fill="#fff"/>
    <circle cx="17" cy="14" r="3.4" fill="var(--red)"/>
  </svg>
  <div class="address">
    Brightway Upkeep Inc.<br>
    417 Harlow Street Suite B<br>
    Cedarbrook, Maryland 21094
  </div>

  <svg class="icon web-icon" viewBox="0 0 34 34" aria-hidden="true">
    <circle cx="17" cy="17" r="16" fill="var(--red)"/>
    <rect x="8" y="9" width="18" height="12" rx="1.5" fill="none" stroke="#fff" stroke-width="2.4"/>
    <path d="M17 21v4M12 26h10" stroke="#fff" stroke-width="2.4" stroke-linecap="round"/>
  </svg>
  <div class="website">www.BrightwayUpkeep.com</div>

  <div class="band-rule"></div>
  <nav class="link-band">
    <span class="band-link" style="left:30px"><span class="dot"></span>Link</span>
    <span class="band-link" style="left:379px"><span class="dot"></span>Link</span>
    <span class="band-link" style="left:700px"><span class="dot"></span>Link</span>
  </nav>

  <p class="disclaimer">This email contains confidential information and may be legally privileged. If you have received it in error, you may not read, use, copy or disclose this email or its attachments. In that case, please let us know immediately by reply email and then delete this email from your system. This information may be subject to a non disclosure regime. Please contact us before this document is released to any third party, including the Inland Revenue Department. While we use standard virus checking software, we accept no responsibility for viruses or anything similar in this email or any attachments. We also do not accept any responsibility for any changes to, or interception of, this email or any attachment after it leaves our information systems. If you are interested in establishing more secure communications between us, please contact our systems administrator by email at admin@brightwayupkeep.com</p>
</section>
</body>
</html>
```